Killer design for artists website and gallery

Current website is www.pebblenook.com.au and it runs on a very simple Wordpress standard theme. We would like a theme designed and customised to suit the branding and style. We have someone who will then code the site in HTML and CSS into Wordpress.

The general theme and branding can be seen on the site at the moment. Please note I have now uploaded full size files into the project. The website background files are for reference only as they are currently on the site. There is no requirement to use them in the new design, however the logo must be as per the attachment.. Please submit a home page/main gallery, and we will request additional pages (about us, other galleries etc.) from those designers we like during the project time.
Updates

Please note I have now uploaded full size files into the project. The website background files are for reference only as they are currently on the site. There is no requirement to use them in the new design, however the logo must be as per the attachment.

Target Market(s)

sales are only in Australia, and priced between approx $100 and $1000. Most viewers and buyers are 20-40 years old, and looking for a casual canvas work for home, or a gift.

Industry/Entity Type

Artists

Font styles to use
Serif
Sans Serif

Requirements
Must have
• gallery of images, responsive design, ability to select categories of pictures (see top menu on current site) and have the gallery change to match, colours to match branding and logo.
Nice to have
• simple minimalist style is preferred. More like http://www.tobiasmerlowe.com/ than http://www.harborcanvasco.com.au/ or http://www.vividplume.com.au/
Should not have
• does not need any online store, or shopping cart etc.

```html
<!DOCTYPE html>
<html lang="en">
<head>
<meta charset="utf-8">
<title>Pebble Nook — Beautiful Canvas Art Made In Melbourne</title>
<link rel="stylesheet" href="https://fonts.googleapis.com/css2?family=Open+Sans:wght@300;400;600;700&display=swap">
<style>
  :root{
    --brand-yellow:#f5e81a;
    --ink:#111111;
    --text-grey:#7a7a7a;
    --heading-grey:#666666;
    --rule-grey:#bdbdbd;
    --footer-bg:#000000;
    --footer-text:#c4c4c4;
    --footer-head:#ffffff;
    --frame-grey:#ececec;
  }
  *{box-sizing:border-box;margin:0;padding:0}
  html,body{width:1200px;height:1134px;overflow:hidden;background:#ffffff}
  body{position:relative;font-family:"Open Sans",Arial,sans-serif;color:var(--ink)}
  .abs{position:absolute}

  /* header */
  .nav-bar{left:0;top:51px;width:1200px;height:42px;background:var(--brand-yellow)}
  .brand-box{left:199px;top:26px;width:91px;height:92px;background:var(--ink);border-radius:8px;border:2px solid var(--brand-yellow);
    display:flex;align-items:flex-end;padding:0 0 14px 6px}
  .brand-name{font-size:13px;font-weight:400;color:#ffffff;line-height:15px;letter-spacing:.2px}
  .main-nav{left:318px;top:63px;display:flex;list-style:none}
  .main-nav li{font-size:12px;color:#1a1a1a;margin-right:0}
  .main-nav li.active{font-weight:600;color:#000}
  .search-btn{left:976px;top:61px;width:24px;height:24px;border:1px solid #fff;border-radius:4px}

  .headline{left:0;top:106px;width:1200px;text-align:center;font-size:26.5px;font-weight:400;letter-spacing:-.6px;color:#111}
  .headline span{color:var(--brand-yellow)}

  /* slider */
  .slider{left:199px;top:156px;width:802px;height:241px;border:3px solid var(--ink);background:var(--ink);display:flex}
  .slide{height:100%}
  .slide-hills{width:233px;background:linear-gradient(160deg,#8f96d8 0%,#6d74c2 35%,#b48d4a 60%,#4f5aa6 100%)}
  .slide-shore{width:287px;background:linear-gradient(180deg,#1d3b3a 0%,#2f7a74 35%,#4ba39a 52%,#d79a50 70%,#b8773a 100%)}
  .slide-rain{width:276px;background:linear-gradient(90deg,#2c4f8f 0%,#4f92d3 30%,#3f6fb4 60%,#2a4a86 100%)}
  .slider-dots{left:579px;top:413px;display:flex;gap:7px}
  .slider-dots i{display:block;width:10px;height:10px;background:var(--ink);border:1px solid var(--brand-yellow)}

  /* about */
  .rule-full{left:0;width:1200px;height:1px;background:var(--rule-grey)}
  .rule-accent{top:475px;height:3px;background:var(--brand-yellow)}
  .about-title{left:0;top:463px;width:1200px;text-align:center;font-size:17px;font-weight:700;color:var(--heading-grey);letter-spacing:.5px}
  .title-mask{left:514px;top:460px;width:172px;height:30px;background:#fff}
  .about-copy{left:201px;top:513px;width:800px;font-size:11.6px;font-weight:300;color:var(--text-grey);line-height:14.5px}
  .about-copy p{margin-bottom:7px}
  .about-copy b{font-weight:700;color:#555}

  /* recent works */
  .work{top:638px;width:176px}
  .work-frame{width:176px;height:127px;background:var(--frame-grey);padding:3px}
  .work-image{width:100%;height:100%}
  .work-caption{margin-top:13px;font-size:12px;font-weight:600;color:#1a1a1a;line-height:14.5px}
  .img-market{background:linear-gradient(135deg,#b9a69a 0%,#2e4d8c 45%,#6a5e8d 70%,#c8a070 100%)}
  .img-floor{background:linear-gradient(170deg,#e3e1df 0%,#c9c4c0 35%,#8a4f28 60%,#b57a45 100%)}
  .img-rain{background:linear-gradient(90deg,#2a4e8c,#55a0dc 40%,#3a6cb0 70%,#284884)}
  .img-tree{background:linear-gradient(160deg,#8a91d8 0%,#6e74c4 40%,#c09048 70%,#d9d8f0 100%)}
  .arrow{top:690px;width:14px;height:24px}

  /* footer */
  .site-footer{left:0;top:824px;width:1200px;height:270px;background:var(--footer-bg)}
  .widget{top:57px}
  .widget h3{font-size:11.5px;font-weight:700;color:var(--footer-head);margin-bottom:14px}
  .widget ul{list-style:none}
  .widget li{font-size:11px;font-weight:400;color:var(--footer-text);line-height:18.2px}
  .footer-brand{left:874px;top:50px;width:126px;height:126px;border:1.5px solid #8a8a8a;border-radius:10px;display:flex;align-items:flex-end;padding:0 0 12px 9px}
  .footer-brand span{font-size:19px;font-weight:400;color:#9a9a9a;line-height:21px}
  .social{left:915px;top:188px;display:flex;gap:6px}
  .social i{display:block;width:12px;height:12px;border-radius:50%;background:#6f6f6f}
  .copyright{left:201px;top:1105px;font-size:10.5px;color:#555}
</style>
</head>
<body>
  <header>
    <div class="abs nav-bar"></div>
    <div class="abs brand-box"><span class="brand-name">PEBBLE NOOK</span></div>
    <ul class="abs main-nav">
      <li class="active" style="margin-right:22px">Home</li>
      <li style="margin-right:24px">About</li>
      <li style="margin-right:24px">Cityscapes</li>
      <li style="margin-right:24px">Other Works</li>
      <li style="margin-right:24px">Seacapes</li>
      <li style="margin-right:24px">Testimonials</li>
      <li>Work For Sale</li>
    </ul>
    <div class="abs search-btn">
      <svg width="22" height="22" viewBox="0 0 22 22"><circle cx="10" cy="10" r="4.5" fill="none" stroke="#fff" stroke-width="1.3"/><line x1="13.3" y1="13.3" x2="16.5" y2="16.5" stroke="#fff" stroke-width="1.3"/></svg>
    </div>
  </header>

  <h1 class="abs headline">Beautiful Canvas Art Made In <span>Melbourne</span></h1>

  <section class="abs slider">
    <div class="slide slide-hills" role="img" aria-label="Painting of a golden tree beside blue hills"></div>
    <div class="slide slide-shore" role="img" aria-label="Painting of a figure with an umbrella on a beach"></div>
    <div class="slide slide-rain" role="img" aria-label="Painting of a couple under an umbrella in blue rain"></div>
  </section>
  <div class="abs slider-dots"><i></i><i></i><i></i></div>

  <div class="abs rule-full" style="top:476px"></div>
  <div class="abs rule-accent" style="left:323px;width:191px"></div>
  <div class="abs rule-accent" style="left:686px;width:190px"></div>
  <div class="abs title-mask"></div>
  <h2 class="abs about-title">ABOUT US</h2>

  <div class="abs about-copy">
    <p>Maren Hollis is a local artist who paints with acrylics, specialising in seascapes, landscapes and cityscapes. She has painted for many years and studied under established artists in Melbourne.</p>
    <p>Pebble Nook was established in 2012 by Maren. The website <b>http://www.pebblenook.com.au</b> and page <b>http://www.pinboardly.com/pebblenookau</b> showcase all recent paintings. Commissions are available along with other pieces for sale.</p>
  </div>

  <div class="abs rule-full" style="top:617px"></div>

  <svg class="abs arrow" style="left:198px" viewBox="0 0 14 24"><polyline points="11,2 2,12 11,22" fill="none" stroke="#222" stroke-width="1.2"/></svg>
  <svg class="abs arrow" style="left:988px" viewBox="0 0 14 24"><polyline points="3,2 12,12 3,22" fill="none" stroke="#222" stroke-width="1.2"/></svg>

  <article class="abs work" style="left:230px">
    <div class="work-frame"><div class="work-image img-market" role="img" aria-label="Photo of a market stall with paintings"></div></div>
    <div class="work-caption">North Melbourne Markets</div>
  </article>
  <article class="abs work" style="left:418px">
    <div class="work-frame"><div class="work-image img-floor" role="img" aria-label="Photo of canvases leaning on a wooden floor"></div></div>
    <div class="work-caption">Ready for North Melbourne Market Tomorrow</div>
  </article>
  <article class="abs work" style="left:605px">
    <div class="work-frame"><div class="work-image img-rain" role="img" aria-label="Painting of a couple under an umbrella in the rain"></div></div>
    <div class="work-caption">Into The Rain</div>
  </article>
  <article class="abs work" style="left:792px">
    <div class="work-frame"><div class="work-image img-tree" role="img" aria-label="Painting of golden trees and hills"></div></div>
    <div class="work-caption">Wood and Trees</div>
  </article>

  <footer class="abs site-footer">
    <div class="abs widget" style="left:200px">
      <h3>Recent Posts</h3>
      <ul style="margin-left:-2px;width:140px">
        <li>North Melbourne Markets</li>
        <li>Ready for North Melbourne Market Tomorrow</li>
        <li>Wood and Trees</li>
        <li>Into The Rain</li>
        <li>My newest seascape</li>
      </ul>
    </div>
    <div class="abs widget" style="left:397px">
      <h3 style="margin-bottom:11px">Archives</h3>
      <ul>
        <li>June 2013</li><li>March 2013</li><li>February 2013</li><li>November 2012</li><li>October 2012</li><li>September 2012</li><li>August 2012</li><li>July 2012</li><li>May 2012</li>
      </ul>
    </div>
    <div class="abs widget" style="left:542px">
      <h3 style="margin-bottom:16px">Categories</h3>
      <ul>
        <li>art</li><li>Cityscapes</li><li>market</li><li>Other Work</li><li>Seascapes</li><li>social</li><li>wedding</li><li>work in progress</li>
      </ul>
    </div>
    <div class="abs widget" style="left:686px">
      <h3 style="margin-bottom:11px">Meta</h3>
      <ul>
        <li>Register</li><li>Log in</li><li>Entries RSS</li><li>Comments RSS</li><li>Blog at Inkwell.com.</li>
      </ul>
    </div>
    <div class="abs footer-brand"><span>PEBBLE NOOK</span></div>
    <div class="abs social"><i></i><i></i><i></i></div>
  </footer>

  <p class="abs copyright">© Copyright PebbleNook 2014</p>
</body>
</html>
```